R & T Summit Construction Business Card ideas

We want a business card to represents our company in a way that looks professional but is also a business card that is unique!

Industry/Entity Type

Construction Company

Contact Information for Business Card

open to all design ideas, just want to be able to see different options to choose from in either color or grayscale.

Requirements
Must have
• Our names and phone numbers
• Nolan Pritchett 512-804-2271
• Curtis Hale 512-693-1804
• Business logo

```html
<!DOCTYPE html>
<html lang="en">
<head>
<meta charset="utf-8">
<title>R &amp; T Summit Construction – Business Card</title>
<link href="https://fonts.googleapis.com/css2?family=Montserrat:wght@300;600&display=swap" rel="stylesheet">
<style>
  :root {
    --page-bg: #e6e8ec;
    --card-white: #ffffff;
    --ink: #000000;
    --faint: #e4e4e4;
    --divider: #ffffff;
  }
  html, body {
    margin: 0;
    padding: 0;
    width: 1200px;
    height: 800px;
    overflow: hidden;
    background: var(--page-bg);
  }
  .canvas {
    width: 1200px;
    height: 800px;
    display: flex;
    align-items: center;
    justify-content: center;
  }
  .card {
    position: relative;
    width: 396px;
    height: 700px;
    background: var(--card-white);
    border: 3px solid var(--ink);
    border-radius: 22px;
    overflow: hidden;
    box-sizing: border-box;
    font-family: "Montserrat", sans-serif;
  }
  .card__crest-area {
    position: absolute;
    top: 0;
    left: 0;
    width: 100%;
    height: 122px;
    background: linear-gradient(to bottom, var(--faint), var(--card-white));
  }
  .brand {
    position: absolute;
    top: 318px;
    left: 0;
    width: 100%;
    display: flex;
    align-items: center;
    justify-content: center;
    gap: 12px;
  }
  .brand__mark {
    width: 22px;
    height: 22px;
    background: var(--ink);
  }
  .brand__name {
    font-weight: 600;
    font-size: 21px;
    line-height: 1.15;
    color: var(--ink);
    text-transform: uppercase;
    letter-spacing: 0.5px;
  }
  .contact {
    position: absolute;
    left: 0;
    width: 100%;
    background: var(--ink);
    color: var(--card-white);
    text-align: center;
    box-sizing: border-box;
  }
  .contact--first { top: 413px; height: 123px; padding-top: 22px; }
  .contact--second { top: 539px; height: 127px; padding-top: 24px; }
  .contact__divider {
    position: absolute;
    top: 536px;
    left: 0;
    width: 100%;
    height: 3px;
    background: var(--divider);
  }
  .contact__name {
    font-weight: 600;
    font-size: 30px;
    letter-spacing: 2px;
    text-transform: uppercase;
    margin: 0;
  }
  .contact__phone {
    margin-top: 10px;
    display: flex;
    align-items: center;
    justify-content: center;
    gap: 6px;
    font-weight: 300;
    font-size: 22px;
    letter-spacing: 0.5px;
  }
  .contact__phone svg { width: 26px; height: 26px; }
</style>
</head>
<body>
  <div class="canvas">
    <div class="card">
      <div class="card__crest-area" role="img" aria-label="Faint company emblem decoration"></div>

      <div class="brand">
        <span class="brand__mark"></span>
        <span class="brand__name">R &amp; T Summit<br>Construction</span>
      </div>

      <div class="contact contact--first">
        <p class="contact__name">Nolan Pritchett</p>
        <div class="contact__phone">
          <svg viewBox="0 0 26 26" aria-hidden="true">
            <circle cx="13" cy="13" r="11.5" fill="none" stroke="#fff" stroke-width="1.6"/>
            <rect x="9" y="6.5" width="8" height="13" rx="1.5" fill="none" stroke="#fff" stroke-width="1.6"/>
            <line x1="11.5" y1="17" x2="14.5" y2="17" stroke="#fff" stroke-width="1.4"/>
          </svg>
          <span>512-804-2271</span>
        </div>
      </div>

      <div class="contact__divider"></div>

      <div class="contact contact--second">
        <p class="contact__name">Curtis Hale</p>
        <div class="contact__phone">
          <svg viewBox="0 0 26 26" aria-hidden="true">
            <circle cx="13" cy="13" r="11.5" fill="none" stroke="#fff" stroke-width="1.6"/>
            <rect x="9" y="6.5" width="8" height="13" rx="1.5" fill="none" stroke="#fff" stroke-width="1.6"/>
            <line x1="11.5" y1="17" x2="14.5" y2="17" stroke="#fff" stroke-width="1.4"/>
          </svg>
          <span>512-693-1804</span>
        </div>
      </div>
    </div>
  </div>
</body>
</html>
```